Business Card Design Project

We need a simple business card design that uses our current logo.
We need to have the current logo put into a high res format.
We need to have 1 card made with contact information.
We will supply the information for the 4 employees.
Industry/Entity Type
Business
Requirements
Must have
- The contact information is as follows:
Paul Vardenko
Producer/CEO
c. 949-555-0148
f. 650-555-0193
paulv@lanternyardstudio.example
Mel Trosgaard, CFO
c. 949-555-0172
f. 650-555-0193
melt@lanternyardstudio.example
Paul Brenneky, PR
c. 267-555-0126
f. 650-555-0193
pbrenneky@lanternyardstudio.example
Dale Furnow, Producer
c. 949-555-0164
f. 650-555-0193
dalef@lanternyardstudio.example
The address for all cards is:
318 W Calle Norvista #2715, San Clemente, CA 92631

```html
<!DOCTYPE html>
<html lang="en">
<head>
<meta charset="UTF-8">
<title>Lantern Yard Studio — Business Card</title>
<link rel="stylesheet" href="https://fonts.googleapis.com/css2?family=Arimo:wght@400;700&display=swap">
<style>
  :root {
    --ink: #000000;
    --paper: #ffffff;
    --brand-blue: #4aa3e3;
    --band-blue: #3d9be0;
  }
  * { margin: 0; padding: 0; box-sizing: border-box; }
  html, body {
    width: 1200px;
    height: 686px;
    overflow: hidden;
    background: var(--paper);
  }
  .card {
    position: relative;
    width: 1200px;
    height: 686px;
    background: var(--paper);
    font-family: "Arimo", Arial, sans-serif;
  }
  .masthead {
    position: absolute;
    left: 0; top: 0;
    width: 1200px;
    height: 200px;
    background: var(--ink);
    border-bottom: 9px solid var(--band-blue);
    height: 209px;
    text-align: center;
  }
  .company-name {
    position: absolute;
    left: 0; right: 0;
    top: 52px;
    font-size: 64px;
    font-weight: 700;
    letter-spacing: 1px;
    text-transform: uppercase;
    color: var(--brand-blue);
    line-height: 1;
  }
  .address {
    position: absolute;
    left: 0; right: 0;
    top: 140px;
    font-size: 29px;
    font-weight: 700;
    letter-spacing: 0.5px;
    color: var(--paper);
    line-height: 1;
  }
  .person {
    position: absolute;
    left: 0; right: 0;
    top: 290px;
    text-align: center;
    color: var(--brand-blue);
  }
  .person-name {
    font-size: 102px;
    font-weight: 700;
    line-height: 1;
    letter-spacing: -1px;
  }
  .person-title {
    margin-top: 22px;
    font-size: 52px;
    font-weight: 400;
    line-height: 1;
  }
  .contact-band {
    position: absolute;
    left: 0; bottom: 0;
    width: 1200px;
    height: 72px;
    background: var(--band-blue);
    display: flex;
    align-items: center;
    justify-content: center;
    gap: 26px;
    color: var(--paper);
    font-size: 31px;
    font-weight: 400;
    white-space: nowrap;
  }
  .contact-divider {
    font-size: 34px;
  }
</style>
</head>
<body>
  <div class="card">
    <header class="masthead">
      <div class="company-name">Lantern Yard Studio</div>
      <div class="address">318 W Calle Norvista #2715, San Clemente, CA 92631</div>
    </header>

    <section class="person">
      <h1 class="person-name">Paul Vardenko</h1>
      <p class="person-title">Producer/CEO</p>
    </section>

    <footer class="contact-band">
      <span class="contact-item">c. 949-555-0148</span>
      <span class="contact-divider">|</span>
      <span class="contact-item">f. 650-555-0193</span>
      <span class="contact-divider">|</span>
      <span class="contact-item">paulv@lanternyardstudio.example</span>
    </footer>
  </div>
</body>
</html>
```